Small corporate website template design

I need a couple templates designed for a small corporate website. The corporate site reflects the existence of the parent company which will own various brands/services that have their own websites, so it will mainly be used to present who we are, what we do, what is happening (news/events), how to contact us, link off to our other brand/service sites, as well as post information for public relations, investors, and job opportunities.

The company name is Vornelight LLC (www.vornelight.example), and the name is representative of stratified layers of interconnected digital services. The corporate site is not expected to generate a bunch of fanfare - that honor will be reserved for the externally linked brand/service sites.

The provided logo may be manipulated in color, size, shape, positioning, etc. to get it to fit with the design, but should be integrated in some way.

What we are looking for is a home page layout as well as a template for an inner page whereby the navigation/logo, etc may be diminished to some extent for the inner pages. We are also interested in reusable elements such as dividers, content containers, etc. in order to represent the types of information described above that we would like to present as described above.

We are particularly interested in consistency of design elements, conservative use of color (including consideration of accessibility concerns), judicious use of whitespace in favor of simplified messaging, and something lending itself well to internationalization/translation.

Target Market(s)

Small business owners, entrepreneurs (B2B)

Number of Pages Required

2 page

Font styles to use
Sans Serif

Requirements
Must have
• See the attached PDF with the logo concept, color swatches, and comparative sites.

```html
<!DOCTYPE html>
<html lang="en">
<head>
<meta charset="utf-8">
<title>Vornelight LLC</title>
<link rel="stylesheet" href="https://fonts.googleapis.com/css2?family=Montserrat:wght@400;600;700&family=Open+Sans:wght@400;600&display=swap">
<style>
  :root {
    --navy: #1d3461;
    --blue: #4a7fc1;
    --deep-blue: #1b3f7e;
    --green: #7cbb14;
    --footer-green: #79b51c;
    --orange: #f7860f;
    --hex: #4f82c4;
    --text: #222;
    --muted: #7a7a7a;
    --light: #f4f4f6;
    --white: #fff;
  }
  * { box-sizing: border-box; margin: 0; padding: 0; }
  html, body { width: 732px; height: 1200px; overflow: hidden; }
  body { position: relative; font-family: "Open Sans", sans-serif; color: var(--text); background: var(--white); }

  .hero { position: absolute; left: 0; top: 0; width: 732px; height: 430px;
    background: linear-gradient(180deg, #f7f7f9 0%, #eeeef1 100%); }
  .brand { position: absolute; left: 76px; top: 30px; display: flex; align-items: center; gap: 8px; }
  .brand-mark { width: 26px; height: 26px; background: #111; border-radius: 50%; }
  .brand-name { font-family: "Montserrat", sans-serif; font-weight: 600; font-size: 17px; color: #111; }
  .main-nav { position: absolute; top: 32px; left: 264px; display: flex; gap: 0; font-family: "Montserrat", sans-serif; font-size: 9px; }
  .main-nav a { position: absolute; white-space: nowrap; text-decoration: none; color: #333; }
  .main-nav a.active { color: var(--blue); }

  .hero-title { position: absolute; left: 70px; top: 160px; font-family: "Montserrat", sans-serif; font-weight: 700; font-size: 20.5px; line-height: 25px; color: var(--navy); }
  .hero-title .accent { color: var(--blue); }
  .btn { position: absolute; display: flex; align-items: center; justify-content: center; font-family: "Open Sans", sans-serif; font-weight: 600; text-decoration: none; border-radius: 16px; }
  .btn-green { left: 70px; top: 251px; width: 107px; height: 30px; background: var(--green); color: var(--white); font-size: 11px; }
  .hero-visual { position: absolute; left: 392px; top: 76px; width: 272px; height: 272px; border-radius: 50%;
    background: radial-gradient(circle at 45% 40%, #c05bd6 0%, #6b4fc9 35%, #3fb4d8 65%, rgba(200,200,215,0.35) 75%, rgba(240,240,244,0) 78%); }
  .slider-dots { position: absolute; left: 336px; top: 352px; display: flex; align-items: center; gap: 4px; }
  .slider-dots .arrow { width: 11px; height: 11px; border-radius: 50%; background: #8a8a8a; }
  .slider-dots .dot { width: 5px; height: 5px; border-radius: 50%; background: #c4c4c4; }
  .slider-dots .dot.on { background: #888; }

  .who-band { position: absolute; left: 0; top: 370px; width: 732px; height: 340px; }
  .who-content { position: absolute; left: 0; top: 464px; width: 732px; text-align: center; color: var(--white); }
  .who-content h2 { font-family: "Montserrat", sans-serif; font-weight: 700; font-size: 19px; letter-spacing: 0.3px; }
  .who-content p { width: 450px; margin: 14px auto 0; font-size: 9.2px; line-height: 15.2px; }
  .btn-outline { left: 307px; top: 573px; width: 106px; height: 30px; border: 1.5px solid var(--white); color: var(--white); font-size: 11px; }

  .contact-visual { position: absolute; left: 66px; top: 692px; width: 258px; height: 278px;
    background: linear-gradient(135deg, #e9e9ea 0%, #bdbdc0 50%, #5d5d60 100%); border-radius: 4px; }
  .contact { position: absolute; left: 373px; top: 748px; width: 290px; }
  .contact h2 { font-family: "Montserrat", sans-serif; font-weight: 700; font-size: 18px; color: var(--navy); }
  .contact .lead { margin-top: 6px; font-size: 9.2px; line-height: 15px; color: var(--muted); }
  .contact-list { list-style: none; margin-top: 11px; }
  .contact-list li { display: flex; align-items: center; gap: 8px; height: 29px; font-size: 9.6px; color: #222; font-family: "Roboto", "Open Sans", sans-serif; }
  .contact-list svg { width: 28px; height: 26px; flex: none; }
  .btn-orange { left: 371px; top: 918px; width: 99px; height: 26px; background: var(--orange); color: var(--white); font-size: 9.6px; font-weight: 400; }

  .footer-band { position: absolute; left: 0; top: 968px; width: 732px; height: 232px; }
  .footer-brand { position: absolute; left: 96px; top: 1060px; font-family: "Montserrat", sans-serif; font-weight: 600; font-size: 14px; color: #b4d977; }
  .social { position: absolute; left: 89px; top: 1107px; display: flex; gap: 5px; }
  .social span { width: 21px; height: 21px; border: 1px solid var(--white); border-radius: 50%; }
  .footer-col { position: absolute; top: 1034px; color: var(--white); }
  .footer-col h3 { font-family: "Montserrat", sans-serif; font-weight: 600; font-size: 10.5px; margin-bottom: 10px; }
  .footer-col ul { list-style: none; }
  .footer-col li { font-size: 9.6px; line-height: 18.6px; }
  .footer-col.blogs li { font-size: 7.6px; line-height: 11px; margin-bottom: 8px; padding-left: 9px; position: relative; width: 160px; }
  .footer-col.blogs li::before { content: "›"; position: absolute; left: 0; top: -2px; font-size: 11px; }
  .footer-rule { position: absolute; left: 72px; top: 1166px; width: 582px; height: 1px; background: rgba(255,255,255,0.35); }
  .copyright { position: absolute; left: 0; top: 1177px; width: 732px; text-align: center; font-size: 7.4px; color: #d9ecbb; }
</style>
</head>
<body>
  <header class="hero">
    <div class="brand"><span class="brand-mark"></span><span class="brand-name">Vornelight</span></div>
    <nav class="main-nav">
      <a class="active" style="left:0">HOME</a>
      <a style="left:47px">ABOUT US</a>
      <a style="left:112px">WHY WE ARE</a>
      <a style="left:188px">WHAT WE DO</a>
      <a style="left:265px">NEWS</a>
      <a style="left:311px">JOBS</a>
      <a style="left:355px">CONTACT</a>
    </nav>
    <h1 class="hero-title"><span class="accent">ADAPTIVE SOFTWARE</span><br>TECHNOLOGY FOR<br>THE DIGITAL REVOLUTION</h1>
    <a class="btn btn-green">Learn More</a>
    <div class="hero-visual" role="img" aria-label="Glowing network sphere of connected nodes in purple and cyan"></div>
    <div class="slider-dots"><span class="arrow"></span><span class="dot on"></span><span class="dot"></span><span class="dot"></span><span class="dot"></span><span class="arrow"></span></div>
  </header>

  <svg class="who-band" viewBox="0 0 732 340" role="img" aria-label="Blue digital network background">
    <defs>
      <linearGradient id="whoGrad" x1="0" y1="0" x2="1" y2="1">
        <stop offset="0" stop-color="#2a5aa3"/>
        <stop offset="0.6" stop-color="#1b3f7e"/>
        <stop offset="1" stop-color="#0f2550"/>
      </linearGradient>
    </defs>
    <polygon points="0,3 732,50 732,336 0,288" fill="url(#whoGrad)"/>
  </svg>
  <section class="who-content">
    <h2>WHO WE ARE</h2>
    <p>magna nisl nec elit Praesent elementum elit at tellus nec ultricies sit amet porttitor mattis enim In massa libero interdum nec interdum vel blandit sed nulla In ullamcorper est eget tempor cursus neque mi consectetuer mi a ultricies massa est sed nisl Class aptent taciti sociosqu ad litora torquent per conubia nostra per inceptos hymenaeos Proin nulla arcu nonummy luctus dictum ege</p>
  </section>
  <a class="btn btn-outline">Learn More</a>

  <div class="contact-visual" role="img" aria-label="Desk seen from above with laptop, glasses, pen, coffee cup and small plant"></div>
  <section class="contact">
    <h2>CONTACT US</h2>
    <p class="lead">Pellentesque faucibus Ut accumsan ultricies elit Maecenas at justo id velit placerat Aolestie Donec dictum lectus non odio</p>
    <ul class="contact-list">
      <li><svg viewBox="0 0 28 26"><polygon points="7,0 21,0 28,13 21,26 7,26 0,13" fill="var(--hex)"/><path d="M14 6a4 4 0 0 0-4 4c0 3 4 8 4 8s4-5 4-8a4 4 0 0 0-4-4zm0 5.5a1.5 1.5 0 1 1 0-3 1.5 1.5 0 0 1 0 3z" fill="#fff"/></svg>48 Larkmoor Avenue #12 Dellwick 50231</li>
      <li><svg viewBox="0 0 28 26"><polygon points="7,0 21,0 28,13 21,26 7,26 0,13" fill="var(--hex)"/><path d="M10 7l2.5-.5 1.5 3-1.5 1.2c.7 1.6 1.8 2.7 3.3 3.3l1.2-1.5 3 1.5-.5 2.5c-5 .5-9.5-4-9.5-9.5z" fill="none" stroke="#fff" stroke-width="1"/></svg>555.014.2290</li>
      <li><svg viewBox="0 0 28 26"><polygon points="7,0 21,0 28,13 21,26 7,26 0,13" fill="var(--hex)"/><rect x="8.5" y="8.5" width="11" height="8" fill="none" stroke="#fff" stroke-width="1"/><path d="M8.5 8.5l5.5 4.5 5.5-4.5" fill="none" stroke="#fff" stroke-width="1"/></svg>info@vornelight.example</li>
    </ul>
  </section>
  <a class="btn btn-orange">Contact Us Now</a>

  <svg class="footer-band" viewBox="0 0 732 232" aria-hidden="true">
    <polygon points="0,38 732,0 732,232 0,232" fill="var(--footer-green)"/>
  </svg>
  <footer>
    <div class="footer-brand">Vornelight</div>
    <div class="social" aria-label="Social links"><span></span><span></span><span></span><span></span></div>
    <div class="footer-col" style="left:224px">
      <h3>QUICK LINKS</h3>
      <ul><li>About Us</li><li>What We Do</li><li>Who We Are</li><li>Why Us</li></ul>
    </div>
    <div class="footer-col" style="left:354px">
      <h3>RESOURCES</h3>
      <ul><li>News &amp; Blogs</li><li>Team</li><li>Contact Us</li></ul>
    </div>
    <div class="footer-col blogs" style="left:475px">
      <h3>OUR BLOGS</h3>
      <ul>
        <li>Morbi diam mauris viverra in gravida eu mattis in ante Morbi eget arcu</li>
        <li>Morbi porta libero id ullamcorper</li>
        <li>Nonummy nibh ligula pulvinar metus eget consectetuer augue nisi quis lacus</li>
      </ul>
    </div>
    <div class="footer-rule"></div>
    <p class="copyright">© 2018 Vornelight LLC &nbsp;All right reserved</p>
  </footer>
</body>
</html>
```